Brinevale Yacht Management Full Page Ad Flyer

Yacht Management Package also includes the following periodic Monthly services:

Monthly full vessel systems checklist inspections
Diver For Hull Cleaning And Inspection Of Props, Shafts, and Zincs
Interior/Exterior Detailing and scheduled washdowns
Manage Haulout
Pump-out Services
On-call Captain and Crew Services
Updates

Need more time to provide more content to designers and the printing press template file.

Target Market(s)

Vessel owners, motor yachts, sailboats from 25 feet in length up to 125 feet in length. We do not do cruise ships or yachts larger than 125 feet. Someone who has their boat docked at their house or a local marina. We also offer mobile on-site services.

```html
<!DOCTYPE html>
<html lang="en">
<head>
<meta charset="utf-8">
<title>Brinevale Yacht Management – Periodic Monthly Services</title>
<link href="https://fonts.googleapis.com/css2?family=Cinzel:wght@600;700&family=Arimo:wght@600&family=Montserrat:wght@500;600&display=swap" rel="stylesheet">
<style>
  :root{
    --navy:#1f2f6e;
    --sea-deep:#1b6fae;
    --sea:#2b8fcb;
    --sea-light:#47a8dc;
    --band:rgba(18,90,150,0.35);
    --white:#ffffff;
    --ink:#0d0d0d;
  }
  *{margin:0;padding:0;box-sizing:border-box}
  html,body{width:926px;height:1200px;overflow:hidden;background:#fff}
  .flyer{position:relative;width:926px;height:1200px;overflow:hidden;
    background:linear-gradient(180deg,var(--sea-light) 0%,var(--sea) 45%,var(--sea-deep) 100%)}
  .sea-photo{position:absolute;inset:0}
  .header-wave{position:absolute;left:0;top:0;width:926px;height:300px}
  .brand{position:absolute;top:70px;left:0;width:926px;text-align:center;
    font-family:'Cinzel',serif;font-weight:700;color:var(--navy)}
  .brand-name{font-size:66px;letter-spacing:2px;line-height:1}
  .brand-sub{font-size:25px;letter-spacing:6px;margin-top:14px}
  .headline{position:absolute;left:0;width:926px;text-align:center;color:var(--white);
    font-family:'Cinzel',serif;font-weight:700;line-height:1}
  .headline-top{top:318px;font-size:58px}
  .headline-bottom{top:392px;font-size:62px;left:10px}
  .service{position:absolute;display:flex;align-items:center;gap:0}
  .service-icon{width:56px;height:56px;border-radius:50%;background:var(--white);
    border:3px solid var(--ink);box-shadow:0 0 0 3px var(--white);
    display:flex;align-items:center;justify-content:center;flex:none}
  .service-icon svg{width:38px;height:38px}
  .service-text{margin-left:17px;font-family:'Arimo',sans-serif;font-weight:600;
    font-size:16px;line-height:18px;color:var(--white)}
  .band{position:absolute;left:0;top:875px;width:926px;height:204px;background:var(--band)}
  .yacht-photo{position:absolute;left:520px;top:880px;width:340px;height:110px;
    transform:rotate(33deg);transform-origin:left top;border-radius:60px 20px 20px 60px;
    background:linear-gradient(90deg,#f4f7fa,#dfe6ee 60%,#c5d2de)}
  .audience{position:absolute;left:125px;top:905px;list-style:none;
    font-family:'Montserrat',sans-serif;font-weight:500;font-size:15px;line-height:20px;color:var(--white)}
  .audience li{display:flex;gap:9px;margin-bottom:20px}
  .audience li svg{flex:none;width:14px;height:14px;margin-top:3px}
  .phone-pill{position:absolute;left:84px;top:1108px;width:276px;height:62px;border-radius:31px;
    background:var(--white);border:3px solid var(--sea-deep);box-shadow:inset 0 0 0 3px var(--white),inset 0 0 0 6px var(--sea-deep);
    display:flex;align-items:center;padding-left:14px;
    font-family:'Montserrat',sans-serif;font-weight:600;font-size:25px;color:var(--ink)}
  .phone-pill .phone-icon{width:30px;height:30px;border:2.5px solid var(--ink);border-radius:50%;
    display:flex;align-items:center;justify-content:center;margin-right:10px}
  .contact{position:absolute;top:1112px;display:flex;align-items:center;gap:7px;
    font-family:'Montserrat',sans-serif;font-weight:500;font-size:19px;color:var(--white)}
  .contact svg{width:17px;height:17px}
  .disclaimer{position:absolute;left:403px;top:1148px;font-family:'Montserrat',sans-serif;
    font-weight:500;font-size:13px;color:var(--white)}
</style>
</head>
<body>
<main class="flyer">
  <div class="sea-photo" role="img" aria-label="Aerial photograph of deep blue rippled ocean water"></div>

  <svg class="header-wave" viewBox="0 0 926 300" preserveAspectRatio="none" aria-hidden="true">
    <path fill="#fff" d="M0 0H926V210C860 255 770 270 700 248L640 245C610 250 590 270 560 276L540 278C580 250 590 230 600 218C560 260 470 290 380 280C300 272 240 235 150 226C90 222 40 240 0 262Z"/>
    <path fill="#fff" d="M0 210C60 200 150 195 200 205C140 200 60 210 0 230Z"/>
  </svg>

  <header class="brand">
    <div class="brand-name">BRINEVALE</div>
    <div class="brand-sub">YACHT MANAGEMENT</div>
  </header>

  <h1 class="headline headline-top">PERIODIC</h1>
  <h1 class="headline headline-bottom">MONTHLY SERVICES:</h1>

  <div class="service" style="left:99px;top:527px">
    <div class="service-icon"><svg viewBox="0 0 40 40" fill="none" stroke="#1b6fae" stroke-width="3"><circle cx="17" cy="17" r="11"/><path d="M25 25L35 35" stroke-linecap="round"/><path d="M11 19h12l-3 3h-7z" stroke-width="1.5"/></svg></div>
    <p class="service-text">Monthly full vessel systems<br>checklist inspections</p>
  </div>
  <div class="service" style="left:520px;top:522px">
    <div class="service-icon"><svg viewBox="0 0 40 40" fill="#1b6fae"><circle cx="20" cy="14" r="9" fill="none" stroke="#1b6fae" stroke-width="3"/><path d="M7 36c0-8 6-12 13-12s13 4 13 12z"/></svg></div>
    <p class="service-text">Diver For Hull Cleaning<br>&amp; Inspection Of Props,<br>Shafts, and Zincs</p>
  </div>
  <div class="service" style="left:99px;top:643px">
    <div class="service-icon"><svg viewBox="0 0 40 40" fill="#1b6fae"><path d="M20 5l2 5 5 2-5 2-2 5-2-5-5-2 5-2z"/><path d="M4 28h30l-4 5H8z"/><path d="M12 28l4-4h10l3 4z"/></svg></div>
    <p class="service-text">Interior/Exterior Detailing<br>&amp; scheduled washdowns</p>
  </div>
  <div class="service" style="left:520px;top:643px">
    <div class="service-icon"><svg viewBox="0 0 40 40" fill="none" stroke="#1b6fae" stroke-width="2.5"><path d="M6 34V8h28v26"/><path d="M6 12h28"/><path d="M10 22h20l-3 6H13z" fill="#1b6fae"/><circle cx="9" cy="35" r="2"/><circle cx="31" cy="35" r="2"/></svg></div>
    <p class="service-text">Manage<br>Haulout</p>
  </div>
  <div class="service" style="left:99px;top:760px">
    <div class="service-icon"><svg viewBox="0 0 40 40" fill="none" stroke="#1b6fae" stroke-width="2.5"><path d="M6 24h28l-5 6H10z" fill="#1b6fae"/><path d="M13 24l3-6h10l4 6"/><path d="M4 34c4-3 8 3 12 0s8 3 12 0 6 2 8 0"/></svg></div>
    <p class="service-text">Pump-out<br>Services</p>
  </div>
  <div class="service" style="left:520px;top:760px">
    <div class="service-icon"><svg viewBox="0 0 40 40" fill="none" stroke="#1b6fae" stroke-width="2.5"><path d="M7 14c6-6 20-6 26 0l-3 5H10z" fill="#1b6fae"/><circle cx="20" cy="29" r="6"/><path d="M20 20v18M11 29h18"/></svg></div>
    <p class="service-text">On-call Captain<br>&amp; Crew Services</p>
  </div>

  <div class="band"></div>
  <div class="yacht-photo" role="img" aria-label="Aerial photograph of a white motor yacht cruising on blue water"></div>

  <ul class="audience">
    <li><svg viewBox="0 0 14 14"><circle cx="7" cy="7" r="7" fill="#fff"/><path d="M3.5 7.2l2.3 2.3 4.5-4.6" fill="none" stroke="#1b6fae" stroke-width="2"/></svg><span>Vessel, motor yachts, sailboats from<br>25 ft in length up to 125 ft in length.</span></li>
    <li><svg viewBox="0 0 14 14"><circle cx="7" cy="7" r="7" fill="#fff"/><path d="M3.5 7.2l2.3 2.3 4.5-4.6" fill="none" stroke="#1b6fae" stroke-width="2"/></svg><span>Someone who has their boat docked<br>at their house or a local marina.</span></li>
    <li><svg viewBox="0 0 14 14"><circle cx="7" cy="7" r="7" fill="#fff"/><path d="M3.5 7.2l2.3 2.3 4.5-4.6" fill="none" stroke="#1b6fae" stroke-width="2"/></svg><span>We also offer mobile on-site services.</span></li>
  </ul>

  <div class="phone-pill">
    <span class="phone-icon"><svg viewBox="0 0 20 20" width="16" height="16"><path d="M5 2l3 4-2 2c1 2 3 4 5 5l2-2 4 3-2 3C9 17 3 11 2 5z" fill="none" stroke="#0d0d0d" stroke-width="1.8"/></svg></span>
    555-204-0188
  </div>

  <div class="contact" style="left:408px">
    <svg viewBox="0 0 18 18"><circle cx="9" cy="9" r="9" fill="#fff"/><rect x="4" y="5.5" width="10" height="7" rx="1" fill="#1b6fae"/><path d="M4.5 6l4.5 3.5L13.5 6" stroke="#fff" stroke-width="1" fill="none"/></svg>
    hello@brinevale.com
  </div>
  <div class="contact" style="left:640px">
    <svg viewBox="0 0 18 18" fill="none" stroke="#fff" stroke-width="1.3"><circle cx="9" cy="9" r="8"/><ellipse cx="9" cy="9" rx="3.5" ry="8"/><path d="M1 9h16M3 5h12M3 13h12"/></svg>
    www.brinevale.com
  </div>
  <p class="disclaimer">We do not do cruise ships or yachts larger than 125 feet.</p>
</main>
</body>
</html>
```